Pest Control Company needs business card!

Hi there, we need a business card designed for our new Pest Control Company. Ideally this card will be simple, yet feel elegant and high end. We want to use the colours Orange, Black and White. Please see our attached logo for the exact colours.

Business card details:

Phone - 0461 275 804
Name - Gavin Holloway
Email - Info@steadfastverminguard.com.au

We would also like to include the following list with dot points:

SERVICES / INSPECTIONS

Termites, Wood Borers, Ants, Cockroaches, Spiders, Fleas, Mice, Rats, Bed Bugs, & More!

```html
<!DOCTYPE html>
<html lang="en">
<head>
<meta charset="utf-8">
<title>Steadfast Vermin Guard – Business Card</title>
<link href="https://fonts.googleapis.com/css2?family=Mulish:wght@300;400;800;900&display=swap" rel="stylesheet">
<style>
  :root {
    --stage: #dedede;
    --orange: #e8901e;
    --white: #f4f4f2;
    --ink: #161616;
    --paper-text: #ffffff;
    --card-shadow: 0 18px 40px rgba(0,0,0,0.18);
  }
  html, body {
    margin: 0;
    width: 1200px;
    height: 900px;
    overflow: hidden;
    background: var(--stage);
    font-family: "Mulish", Arial, sans-serif;
  }
  .stage {
    position: relative;
    width: 1200px;
    height: 900px;
    display: flex;
    align-items: center;
    justify-content: center;
    gap: 40px;
  }
  .card {
    position: relative;
    width: 530px;
    height: 342px;
    flex: none;
    box-sizing: border-box;
    box-shadow: var(--card-shadow);
  }
  .card--back {
    background: var(--orange);
    color: var(--paper-text);
    padding: 36px 40px;
  }
  .card--front {
    background: var(--white);
    display: flex;
    align-items: center;
    justify-content: center;
    padding: 0 40px;
  }
  .brand {
    display: flex;
    align-items: center;
    gap: 10px;
    font-weight: 800;
    text-transform: uppercase;
    line-height: 1;
    white-space: nowrap;
  }
  .brand__dot {
    border-radius: 50%;
    flex: none;
  }
  .brand--small {
    font-size: 19px;
    letter-spacing: 0.5px;
    margin-bottom: 20px;
  }
  .brand--small .brand__dot {
    width: 15px;
    height: 15px;
    background: var(--paper-text);
  }
  .brand--large {
    color: var(--ink);
    font-size: 30px;
    letter-spacing: 0.5px;
    gap: 14px;
    justify-content: center;
  }
  .brand--large .brand__dot {
    width: 24px;
    height: 24px;
    background: var(--ink);
  }
  .contact__name {
    font-weight: 800;
    font-size: 22px;
    margin: 0 0 8px;
  }
  .contact__line {
    font-weight: 300;
    font-size: 19px;
    margin: 0 0 3px;
  }
  .services {
    margin-top: 26px;
  }
  .services__label {
    font-weight: 300;
    font-size: 18px;
    margin: 0 0 6px;
  }
  .services__rule {
    border: 0;
    border-top: 1px solid var(--paper-text);
    margin: 0 0 10px;
  }
  .services__list {
    font-weight: 800;
    font-size: 16px;
    line-height: 1.4;
    margin: 0;
  }
</style>
</head>
<body>
  <main class="stage">
    <section class="card card--back" aria-label="Business card back">
      <div class="brand brand--small">
        <span class="brand__dot"></span>
        <span class="brand__name">Steadfast Vermin Guard</span>
      </div>
      <div class="contact">
        <p class="contact__name">Gavin Holloway</p>
        <p class="contact__line">0461 275 804</p>
        <p class="contact__line">Info@steadfastverminguard.com.au</p>
      </div>
      <div class="services">
        <p class="services__label">Services</p>
        <hr class="services__rule">
        <p class="services__list">Termites, Wood Borers, Ants, Cockroaches, Spiders, Fleas<br>Mice, Rats, Bed Bugs, &amp; More!</p>
      </div>
    </section>

    <section class="card card--front" aria-label="Business card front">
      <div class="brand brand--large">
        <span class="brand__dot"></span>
        <span class="brand__name">Steadfast Vermin Guard</span>
      </div>
    </section>
  </main>
</body>
</html>
```